Wattlegrove Campus Lodgings needs a business card design

Hi Guys,

We are a Student Accommodation company in Australia. We already have a logo which I will submit.

I will require the design of the business cards from you.

I am after something that looks clean, modern and that people feel interested and actually want to contact us.

We would like to see designs that are innovative.

On the business cards I will require to have:

Employee Name
Position
Phone number
Email
Facebook page

I hope you can help me with this project guys as I have heard really good things from you.

```html
<!DOCTYPE html>
<html lang="en">
<head>
<meta charset="utf-8">
<title>Wattlegrove Campus Lodgings – Business Card</title>
<link href="https://fonts.googleapis.com/css2?family=Arimo:ital,wght@0,400;0,700;1,400&display=swap" rel="stylesheet">
<style>
  :root {
    --backdrop: #9b9b9b;
    --card-white: #f4f4f4;
    --brand-green: #0b7f12;
    --brand-green-deep: #06700c;
    --brand-green-light: #1a9a22;
    --brand-gold: #f0b323;
    --text-grey: #555555;
  }
  * { margin: 0; padding: 0; box-sizing: border-box; }
  html, body {
    width: 1200px; height: 720px; overflow: hidden;
    background: var(--backdrop);
    font-family: "Arimo", Arial, sans-serif;
  }
  .canvas {
    position: relative; width: 1200px; height: 720px;
    display: flex; align-items: center; justify-content: center; gap: 60px;
  }
  .card {
    position: relative; width: 525px; height: 300px; overflow: hidden;
    box-shadow: 0 6px 18px rgba(0,0,0,0.25);
  }
  .card-front { background: linear-gradient(160deg, #ffffff 0%, var(--card-white) 70%); }
  .card-front .swoosh { position: absolute; inset: 0; width: 100%; height: 100%; }

  .contact-block { position: absolute; left: 40px; top: 42px; }
  .person-name {
    font-weight: 700; font-size: 22px; color: var(--brand-green); letter-spacing: 0.2px;
  }
  .person-role { font-style: italic; font-size: 13px; color: var(--text-grey); margin-top: 2px; }
  .contact-list { list-style: none; margin-top: 16px; }
  .contact-list li {
    display: flex; align-items: center; gap: 10px;
    font-size: 13.5px; color: var(--text-grey); line-height: 22px;
  }
  .contact-icon { width: 13px; height: 13px; flex: none; }

  .brand-lockup {
    position: absolute; right: 34px; top: 118px;
    display: flex; align-items: center; gap: 10px;
  }
  .brand-square { width: 18px; height: 18px; background: var(--brand-gold); flex: none; }
  .brand-name {
    font-weight: 700; font-size: 19px; line-height: 1.15; color: var(--brand-green);
    text-transform: uppercase; letter-spacing: 0.5px;
  }

  .card-back {
    background: linear-gradient(135deg, var(--brand-green-light) 0%, var(--brand-green) 55%, var(--brand-green-deep) 100%);
    display: flex; align-items: center; justify-content: center;
  }
  .card-back .back-field { position: absolute; inset: 0; }
  .card-back .brand-lockup { position: relative; right: auto; top: auto; }
  .card-back .brand-name { color: #ffffff; font-size: 24px; }
</style>
</head>
<body>
<main class="canvas">

  <section class="card card-front" aria-label="Business card front">
    <svg class="swoosh" viewBox="0 0 525 300" preserveAspectRatio="none" aria-hidden="true">
      <path d="M0 118 C 60 190, 180 255, 330 300 L 0 300 Z" fill="var(--brand-gold)"/>
      <path d="M0 128 C 60 200, 175 262, 310 300 L 0 300 Z" fill="#ffffff"/>
      <path d="M0 136 C 60 206, 170 266, 295 300 L 0 300 Z" fill="var(--brand-green)"/>
      <path d="M300 262 C 400 268, 470 282, 525 298 L 525 300 L 300 300 Z" fill="var(--brand-gold)" opacity="0"/>
      <path d="M330 268 C 420 272, 480 284, 525 296 L 525 284 C 470 272, 400 266, 330 268 Z" fill="var(--brand-gold)"/>
    </svg>

    <div class="contact-block">
      <h1 class="person-name">Maren Holloway</h1>
      <p class="person-role">Chief Executive</p>
      <ul class="contact-list">
        <li>
          <svg class="contact-icon" viewBox="0 0 14 14" aria-hidden="true">
            <rect x="3" y="0.8" width="8" height="12.4" rx="1.4" fill="none" stroke="var(--brand-green)" stroke-width="1.4"/>
            <line x1="6" y1="11" x2="8" y2="11" stroke="var(--brand-green)" stroke-width="1.2"/>
          </svg>
          0400 555 017
        </li>
        <li>
          <svg class="contact-icon" viewBox="0 0 14 14" aria-hidden="true">
            <rect x="0.8" y="2.5" width="12.4" height="9" fill="none" stroke="var(--brand-green)" stroke-width="1.4"/>
            <polyline points="1,3 7,8 13,3" fill="none" stroke="var(--brand-green)" stroke-width="1.4"/>
          </svg>
          maren@wattlegrove.com.au
        </li>
        <li>
          <svg class="contact-icon" viewBox="0 0 14 14" aria-hidden="true">
            <rect x="1" y="1" width="12" height="12" fill="var(--brand-green)"/>
          </svg>
          wattlegrove.com.au/community
        </li>
      </ul>
    </div>

    <div class="brand-lockup">
      <span class="brand-square" aria-hidden="true"></span>
      <p class="brand-name">Wattlegrove<br>Campus<br>Lodgings</p>
    </div>
  </section>

  <section class="card card-back" aria-label="Business card back">
    <div class="back-field" role="img" aria-label="Soft green field where faint building-window squares sit behind the brand"></div>
    <div class="brand-lockup">
      <span class="brand-square" aria-hidden="true"></span>
      <p class="brand-name">Wattlegrove<br>Campus<br>Lodgings</p>
    </div>
  </section>

</main>
</body>
</html>
```